Business Card Design for Law firm - already have logo

Now that we have a logo, we need a business card design - our logo is attached -it is salaryman font if that helps - we would like a file that can be uploaded to kellumo (www.kellumo.com) using the logo and with the following information on it:
Dunmore Law Firm, P.C.
Felix Dunmore, Esq.
6718 NE 19th Ave.
Portland, OR 97284
971.555.0142 phone
971.555.0187 fax
fel@dunmore.net
chatline: feldunmore
quill talk: felix.dunmore@quillmail.com
Target Market(s)
our business cards are distributed to corporate executives, technology professionals and healthcare providers
Industry/Entity Type
Business
Look and feel

```html
<!DOCTYPE html>
<html lang="en">
<head>
<meta charset="utf-8">
<title>Dunmore Law Firm, P.C. – Business Card</title>
<link href="https://fonts.googleapis.com/css2?family=PT+Sans:wght@400;700&family=PT+Sans+Narrow:wght@700&display=swap" rel="stylesheet">
<style>
  :root {
    --page: #ffffff;
    --card-black: #0b0b0b;
    --header-top: #262626;
    --header-bottom: #0e0e0e;
    --ink-white: #ffffff;
    --label-grey: #8a8a8a;
    --sheen-dark: #5c5c5c;
    --sheen-mid: #a9a9a9;
    --sheen-light: #b9cdd3;
  }
  html, body {
    margin: 0;
    padding: 0;
    width: 1200px;
    height: 991px;
    overflow: hidden;
    background: var(--page);
  }
  .business-card {
    position: absolute;
    left: 0;
    top: 0;
    width: 1200px;
    height: 991px;
  }
  .brand-name {
    font-family: "PT Sans", Arial, sans-serif;
    font-weight: 700;
    font-size: 46px;
    fill: var(--ink-white);
  }
  .firm-name {
    font-family: "PT Sans Narrow", "Arial Narrow", sans-serif;
    font-weight: 700;
    font-size: 31px;
    fill: var(--ink-white);
  }
  .attorney-name {
    font-family: "PT Sans", Arial, sans-serif;
    font-weight: 700;
    font-size: 22px;
    fill: var(--ink-white);
  }
  .contact-line {
    font-family: "PT Sans", Arial, sans-serif;
    font-size: 12px;
    fill: var(--ink-white);
  }
  .contact-label { fill: var(--label-grey); }
</style>
</head>
<body>
<svg class="business-card" viewBox="0 0 1200 991" xmlns="http://www.w3.org/2000/svg">
  <defs>
    <linearGradient id="sheen" x1="0" y1="0" x2="1" y2="0.3">
      <stop offset="0" stop-color="var(--sheen-dark)"/>
      <stop offset="0.35" stop-color="var(--sheen-mid)"/>
      <stop offset="0.55" stop-color="var(--sheen-light)"/>
      <stop offset="1" stop-color="var(--sheen-mid)"/>
    </linearGradient>
    <linearGradient id="storm" x1="0" y1="0" x2="0" y2="1">
      <stop offset="0" stop-color="var(--header-top)"/>
      <stop offset="1" stop-color="var(--header-bottom)"/>
    </linearGradient>
  </defs>

  <rect class="card-base" x="283" y="319" width="623" height="357" fill="var(--card-black)"/>

  <rect class="header-artwork" x="286" y="322" width="617" height="145" fill="url(#storm)"
        role="img" aria-label="Lightning bolts crackling across a dark night sky"/>

  <rect class="brand-square" x="299" y="420" width="30" height="30" fill="var(--ink-white)"/>
  <text class="brand-name" x="343" y="452">Dunmore</text>

  <rect class="header-rule" x="286" y="469" width="617" height="4" fill="var(--ink-white)"/>

  <path class="sheen-panel" d="M286 476 L838 476 Q560 500 292 672 L286 672 Z" fill="url(#sheen)"/>
  <path class="sheen-edge" d="M838 475 Q560 500 290 674" fill="none" stroke="var(--ink-white)" stroke-width="4"/>

  <text class="firm-name" x="299" y="527">Dunmore Law Firm, P.C.</text>
  <text class="attorney-name" x="862" y="561" text-anchor="end">Felix Dunmore, Esq.</text>

  <text class="contact-line" x="826" y="641" text-anchor="end">6718 NE 19th Ave. Portland, OR 97284 &#160;&#160;I&#160;&#160; <tspan class="contact-label">t:</tspan> 971.555.0142 &#160;&#160;I&#160;&#160; <tspan class="contact-label">f:</tspan> 971.555.0187</text>
  <text class="contact-line" x="868" y="657" text-anchor="end"><tspan class="contact-label">email:</tspan> fel@dunmore.net &#160;&#160;I&#160;&#160; <tspan class="contact-label">chatline:</tspan> feldunmore &#160;&#160;I&#160;&#160; <tspan class="contact-label">quill talk:</tspan> felix.dunmore@quillmail.com</text>
</svg>
</body>
</html>
```